integrative health clinic-Medical massage, acupuncture, chiropractic

we like our logo, but are open to new ideas. We need a new card design. We have added chiropractic and acupuncture that we have put under the name of the business. We are an integrative medical clinic

Target Market(s)

General public, athletes

Contact Information for Business Card

Phone 5055583927
Fax 5055583926
Hours Monday-Friday 9-6
Saturday 10-6
The 20% can be smaller on the back

Colors
3176b5
0355a3

Requirements
Must have
• Logo but am open to ideas
Nice to have
• We are an integrated medical clinic but also want to be personable. We want the card fun and inviting

```html
<!DOCTYPE html>
<html lang="en">
<head>
<meta charset="utf-8">
<title>Cedar Path Wellness – Business Card</title>
<link rel="stylesheet" href="https://fonts.googleapis.com/css2?family=Open+Sans:ital,wght@0,400;0,600;0,700;1,700&family=Montserrat:wght@700&display=swap">
<style>
  :root {
    --blue: #0a3fff;
    --navy: #0c1f86;
    --band: #92b9cb;
    --band-pale: #dde9ef;
    --white: #ffffff;
    --backdrop: #dcdcdc;
  }
  * { margin: 0; padding: 0; box-sizing: border-box; }
  html, body { width: 848px; height: 1200px; overflow: hidden; }
  body {
    background: var(--backdrop);
    font-family: "Open Sans", sans-serif;
    color: var(--navy);
    position: relative;
  }
  .card {
    position: absolute;
    width: 614px;
    height: 372px;
    overflow: hidden;
  }
  .card svg.shapes { position: absolute; inset: 0; width: 100%; height: 100%; }
  .card-front { left: 88px; top: 100px; background: var(--blue); }
  .card-back { left: 89px; top: 736px; background: var(--white); }

  .brand {
    position: absolute;
    left: 0; right: 0;
    top: 158px;
    display: flex;
    align-items: center;
    justify-content: center;
    gap: 10px;
    padding-left: 60px;
  }
  .brand-dot {
    width: 22px; height: 22px;
    border-radius: 50%;
    background: var(--navy);
  }
  .brand-name {
    font-weight: 700;
    font-size: 27px;
    letter-spacing: -0.3px;
    color: var(--navy);
  }

  .person { position: absolute; left: 20px; top: 22px; }
  .person-name { font-size: 21px; font-weight: 400; line-height: 1.2; }
  .person-name strong { font-weight: 700; }
  .person-role { font-size: 20px; line-height: 1.25; }
  .services {
    position: absolute; left: 20px; top: 94px;
    font-size: 15.5px; font-weight: 700; font-style: italic;
    letter-spacing: 0.4px;
  }

  .hours {
    position: absolute; right: 53px; top: 142px;
    text-align: right; font-size: 12.5px; line-height: 20px;
    letter-spacing: 0.3px;
  }
  .contact-row {
    position: absolute; left: 430px; right: 53px;
    display: flex; align-items: flex-start; justify-content: space-between;
    font-size: 12.5px; letter-spacing: 0.3px;
  }
  .contact-phone { top: 195px; }
  .contact-phone .lines { text-align: right; line-height: 21px; }
  .contact-web { top: 251px; align-items: center; }
  .contact-row svg { width: 16px; height: 16px; margin-top: 6px; }
  .contact-web svg { margin-top: 0; }

  .offer {
    position: absolute; left: 417px; top: 341px;
    font-family: "Montserrat", sans-serif;
    font-weight: 700; font-size: 12.5px; letter-spacing: 1.4px;
  }
</style>
</head>
<body>

<section class="card card-front" aria-label="Card front">
  <svg class="shapes" viewBox="0 0 1176 711" preserveAspectRatio="none" aria-hidden="true">
    <polygon fill="var(--white)" points="459,0 866,0 996,228 571,228"/>
    <polygon fill="var(--band)" points="369,228 996,228 861,480 221,480"/>
    <polygon fill="var(--white)" points="221,480 626,480 761,711 339,711"/>
  </svg>
  <div class="brand">
    <span class="brand-dot"></span>
    <span class="brand-name">Cedar Path Wellness</span>
  </div>
</section>

<section class="card card-back" aria-label="Card back">
  <svg class="shapes" viewBox="0 0 1174 711" preserveAspectRatio="none" aria-hidden="true">
    <defs>
      <linearGradient id="band-fade" x1="0" y1="0" x2="0" y2="1">
        <stop offset="0" stop-color="var(--band-pale)"/>
        <stop offset="0.4" stop-color="var(--band)"/>
        <stop offset="0.65" stop-color="var(--band)"/>
        <stop offset="1" stop-color="var(--band-pale)"/>
      </linearGradient>
    </defs>
    <polygon fill="var(--blue)" points="850,0 1174,0 1174,232 967,232"/>
    <polygon fill="url(#band-fade)" points="473,232 1174,232 1174,537 275,537"/>
    <polygon fill="var(--blue)" points="275,537 680,537 780,711 361,711"/>
  </svg>

  <div class="person">
    <p class="person-name">FULL <strong>NAME</strong></p>
    <p class="person-role">Company Designation</p>
  </div>
  <p class="services">CHIROPRACTIC AND ACUPUNCTURE</p>

  <div class="hours">
    <p>MONDAY-FRIDAY 9-6</p>
    <p>SATURDAY 10-6</p>
  </div>

  <div class="contact-row contact-phone">
    <svg viewBox="0 0 16 16" aria-hidden="true">
      <rect x="1" y="0.5" width="14" height="15" rx="2.5" fill="var(--navy)"/>
      <path d="M6 3.5c-1.2.6-1.3 3.2.2 5.6s3.6 3.6 4.7 3l.6-.5-1.5-1.8-.9.4c-.5-.2-1.3-1-1.8-2s-.6-1.9-.3-2.3l.8-.5-.8-2.2z" fill="var(--white)"/>
    </svg>
    <div class="lines">
      <p>5055583927</p>
      <p>5055583926</p>
    </div>
  </div>

  <div class="contact-row contact-web">
    <svg viewBox="0 0 16 16" aria-hidden="true" fill="none" stroke="var(--navy)" stroke-width="1">
      <circle cx="8" cy="8" r="7"/>
      <ellipse cx="8" cy="8" rx="3" ry="7"/>
      <line x1="1" y1="8" x2="15" y2="8"/>
      <line x1="8" y1="1" x2="8" y2="15"/>
      <path d="M2.2 4.5h11.6M2.2 11.5h11.6"/>
    </svg>
    <p>EMAIL-ID</p>
  </div>

  <p class="offer">20% OFF FIRST VISIT</p>
</section>

</body>
</html>
```